NEW YORK Plumbing/utility company 10 year anniversary business card

Looking For simple back and front business card would like to include a few things in description
We offer 24/7 emergency service
residential
commercial
industrial
municipal
services offered
Plumbing
hydro excavation
hydro jetting
Well pumps
Sewer pumps
water mains
sewer mains

```html
<!DOCTYPE html>
<html lang="en">
<head>
<meta charset="utf-8">
<title>Kestrel Ridge Water &amp; Sewer – Business Card</title>
<link href="https://fonts.googleapis.com/css2?family=Source+Sans+3:wght@400;600;700&display=swap" rel="stylesheet">
<style>
  :root {
    --stage: #e2e2e2;
    --card: #f4f5f6;
    --navy: #1c5a97;
    --sky: #2ea3dd;
    --band-dark: #2466a8;
    --cyan: #1f9cc4;
    --red: #e0232b;
  }
  * { box-sizing: border-box; margin: 0; padding: 0; }
  html, body {
    width: 1200px; height: 900px; overflow: hidden;
    background: var(--stage);
    font-family: "Source Sans 3", "Myriad Pro", Arial, sans-serif;
  }
  .card {
    position: absolute; top: 290px;
    width: 540px; height: 320px;
    background: var(--card);
    box-shadow: 0 6px 18px rgba(0,0,0,0.12);
    overflow: hidden;
  }
  .card--front { left: 40px; }
  .card--back { left: 620px; }
  .band-top { position: absolute; top: 0; left: 0; right: 0; height: 12px; background: linear-gradient(90deg, var(--sky), #37b2ea); }
  .band-bottom { position: absolute; bottom: 0; left: 0; right: 0; height: 14px; background: linear-gradient(90deg, #1e5a9c, var(--band-dark)); }

  .brand { display: flex; align-items: center; color: var(--navy); font-weight: 700; text-transform: uppercase; line-height: 1.05; }
  .brand__dot { border-radius: 50%; background: var(--navy); flex: none; }
  .card--front .brand { position: absolute; left: 0; right: 0; top: 112px; justify-content: center; gap: 16px; font-size: 38px; }
  .card--front .brand__dot { width: 56px; height: 56px; }
  .card--back .brand { position: absolute; right: 26px; top: 34px; gap: 8px; font-size: 17px; }
  .card--back .brand__dot { width: 26px; height: 26px; }

  .headline { position: absolute; left: 24px; top: 30px; color: var(--navy); font-weight: 700; font-size: 20px; }
  .markets { position: absolute; left: 40px; top: 62px; list-style: none; }
  .markets li, .services li { color: var(--cyan); font-size: 15px; line-height: 20px; position: relative; padding-left: 14px; }
  .markets li::before, .services li::before {
    content: ""; position: absolute; left: 0; top: 8px; width: 5px; height: 5px; border-radius: 50%; background: var(--red);
  }
  .section-title { position: absolute; left: 40px; top: 150px; color: var(--navy); font-weight: 700; font-size: 19px; }
  .services { position: absolute; left: 50px; top: 178px; list-style: none; display: grid; grid-template-columns: 108px 130px; }
  .services li.wide { grid-column: 2; }

  .contact { position: absolute; right: 26px; top: 200px; text-align: right; color: var(--navy); font-weight: 600; font-size: 14px; line-height: 24px; }
  .contact__line { display: flex; align-items: center; justify-content: flex-end; gap: 6px; }
  .contact svg { width: 12px; height: 12px; }
</style>
</head>
<body>
  <section class="card card--front" aria-label="Card front">
    <div class="band-top"></div>
    <div class="brand"><span class="brand__dot"></span><span>Kestrel Ridge<br>Water &amp; Sewer</span></div>
    <div class="band-bottom"></div>
  </section>

  <section class="card card--back" aria-label="Card back">
    <div class="band-top"></div>
    <h2 class="headline">We Offer 24/7 Emergency Service</h2>
    <ul class="markets">
      <li>Residential</li>
      <li>Commercial</li>
      <li>Industrial</li>
      <li>Municipal</li>
    </ul>
    <h3 class="section-title">Services Offered</h3>
    <ul class="services">
      <li>Plumbing</li><li>Hydro Excavation</li>
      <li>Hydro Jetting</li><li>Well Pumps</li>
      <li>Sewer Pumps</li><li>Water Mains</li>
      <li class="wide">Sewer Mains</li>
    </ul>
    <div class="brand"><span class="brand__dot"></span><span>Kestrel Ridge<br>Water &amp; Sewer</span></div>
    <div class="contact">
      <div class="contact__line">845-555-0142
        <svg viewBox="0 0 12 12" aria-hidden="true"><path d="M2.5 1 L4.5 1 L5.2 3.5 L4 4.5 Q5 7 7.5 8 L8.5 6.8 L11 7.5 L11 9.5 Q10.5 11 9 11 Q1 10 1 2.5 Q1 1 2.5 1 Z" fill="none" stroke="var(--red)" stroke-width="1.2"/></svg>
      </div>
      <div class="contact__line">info@kestrelridgeny.com
        <svg viewBox="0 0 12 12" aria-hidden="true"><rect x="1" y="2.5" width="10" height="7" fill="none" stroke="var(--red)" stroke-width="1.2"/><path d="M1 2.5 L6 6.5 L11 2.5" fill="none" stroke="var(--red)" stroke-width="1.2"/></svg>
      </div>
    </div>
    <div class="band-bottom"></div>
  </section>
</body>
</html>
```